Letter and Envelope Design For Larchmont Realty

Please design a letter and an envelope incorporating our logo (See Attached). We are also launched a business card contest. Since we want them to match, please feel free to submit a design for both the business card and also the letter design and envelope.

Requirements
Must have
• The envelope, the letter and the business cards must match somehow connecting the designs. We want them to have something that holds them together besides the logo.

```html
<!DOCTYPE html>
<html lang="en">
<head>
<meta charset="utf-8">
<title>Larchmont Realty Stationery</title>
<link href="https://fonts.googleapis.com/css2?family=Josefin+Sans:wght@600&family=Nunito+Sans:ital,wght@0,400;0,700;1,400&display=swap" rel="stylesheet">
<style>
  :root {
    --navy: #2c3179;
    --slate: #5b5b5f;
    --mist: #b9babd;
    --paper: #ffffff;
    --backdrop: #eceef0;
    --ink: #4a4a4e;
  }
  * { box-sizing: border-box; margin: 0; padding: 0; }
  html, body { width: 1154px; height: 1200px; overflow: hidden; }
  body { background: var(--backdrop); position: relative; font-family: "Nunito Sans", sans-serif; }

  .sheet { position: absolute; background: var(--paper); box-shadow: 0 3px 8px rgba(0,0,0,.25); overflow: hidden; }
  .band { position: absolute; left: 0; top: 0; width: 100%; display: block; }
  .band .navy { fill: var(--navy); }
  .band .slate { fill: var(--slate); }
  .band .mist { fill: var(--mist); }

  .brand { position: absolute; display: flex; flex-direction: column; align-items: center; }
  .brand-ring { border: 2px solid var(--navy); border-radius: 50%; }
  .brand-name { font-family: "Josefin Sans", sans-serif; font-weight: 600; color: var(--navy); text-transform: uppercase; white-space: nowrap; line-height: 1; }

  /* Letterhead */
  .letterhead { left: 32px; top: 34px; width: 568px; height: 736px; }
  .letterhead .brand { left: 0; right: 0; top: 55px; }
  .letterhead .brand-ring { width: 52px; height: 52px; margin-bottom: 10px; }
  .letterhead .brand-name { font-size: 15px; letter-spacing: 1.6px; }
  .letterhead .footer-rule { position: absolute; left: 0; right: 0; top: 661px; border-top: 1px solid var(--slate); }
  .letterhead .footer { position: absolute; left: 30px; right: 37px; top: 683px; display: flex; justify-content: space-between; font-weight: 700; font-size: 9.5px; line-height: 12px; color: var(--navy); }
  .letterhead .footer .right { text-align: right; }

  /* Business card front */
  .card-front { left: 672px; top: 158px; width: 427px; height: 244px; }
  .card-front .brand { left: 0; right: 0; top: 60px; }
  .card-front .brand-ring { width: 94px; height: 94px; border-width: 3px; margin-bottom: 18px; }
  .card-front .brand-name { font-size: 27px; letter-spacing: 2.6px; }

  /* Business card back */
  .card-back { left: 672px; top: 436px; width: 427px; height: 244px; }
  .card-back .brand { left: 16px; top: 36px; }
  .card-back .brand-ring { width: 34px; height: 34px; margin-bottom: 5px; }
  .card-back .brand-name { font-size: 9.5px; letter-spacing: .8px; }
  .card-back .contact { position: absolute; left: 15px; top: 140px; color: var(--ink); font-size: 9.5px; line-height: 15.5px; }
  .card-back .person { font-family: "Josefin Sans", sans-serif; font-weight: 600; color: var(--navy); font-size: 15px; line-height: 18px; }
  .card-back .role { font-style: italic; font-size: 11.5px; line-height: 15px; margin-bottom: 6px; }
  .card-back .address { margin-top: 6px; }
  .card-back .web { position: absolute; right: 10px; top: 68px; writing-mode: vertical-rl; transform: rotate(180deg); color: var(--navy); font-size: 9px; height: 140px; text-align: center; }

  /* Envelope */
  .envelope { left: 202px; top: 806px; width: 797px; height: 346px; }
  .envelope .brand { left: 15px; top: 70px; }
  .envelope .brand-ring { width: 52px; height: 52px; margin-bottom: 10px; }
  .envelope .brand-name { font-size: 15px; letter-spacing: 1.6px; }
  .envelope .return-address { position: absolute; left: 14px; top: 320px; font-weight: 700; font-size: 12px; color: var(--slate); }
</style>
</head>
<body>

<section class="sheet letterhead" aria-label="Letterhead">
  <svg class="band" viewBox="0 0 568 58" height="58" preserveAspectRatio="none" aria-hidden="true">
    <polygon class="mist" points="0,55 568,48 568,54 0,58"/>
    <polygon class="slate" points="180,51 568,31 568,49"/>
    <polygon class="navy" points="0,0 568,0 568,31 0,55"/>
  </svg>
  <div class="brand">
    <div class="brand-ring"></div>
    <div class="brand-name">Larchmont Realty</div>
  </div>
  <div class="footer-rule"></div>
  <div class="footer">
    <div class="left">(555) 214-7390<br>www.larchmontrealty.com</div>
    <div class="right">48 Linden Court<br>Maple Ridge • State • 54321</div>
  </div>
</section>

<section class="sheet card-front" aria-label="Business card front">
  <svg class="band" viewBox="0 0 427 35" height="35" preserveAspectRatio="none" aria-hidden="true">
    <polygon class="mist" points="0,33 427,29 427,35 0,35"/>
    <polygon class="slate" points="120,29 427,15 427,30"/>
    <polygon class="navy" points="0,0 427,0 427,15 0,33"/>
  </svg>
  <div class="brand">
    <div class="brand-ring"></div>
    <div class="brand-name">Larchmont Realty</div>
  </div>
</section>

<section class="sheet card-back" aria-label="Business card back">
  <svg class="band" viewBox="0 0 427 35" height="35" preserveAspectRatio="none" aria-hidden="true">
    <polygon class="mist" points="0,28 427,33 427,35 0,31"/>
    <polygon class="slate" points="0,14 300,26 0,29"/>
    <polygon class="navy" points="0,0 427,0 427,33 0,14"/>
  </svg>
  <div class="brand">
    <div class="brand-ring"></div>
    <div class="brand-name">Larchmont Realty</div>
  </div>
  <div class="contact">
    <div class="person">Daniel Reyes</div>
    <div class="role">Realtor</div>
    <div>(555) 214-7390</div>
    <div>dreyes@larchmontrealty.com</div>
    <div class="address">48 Linden Court • Maple Ridge • State • 54321</div>
  </div>
  <div class="web">www.larchmontrealty.com</div>
</section>

<section class="sheet envelope" aria-label="Envelope">
  <svg class="band" viewBox="0 0 797 67" height="67" preserveAspectRatio="none" aria-hidden="true">
    <polygon class="mist" points="0,58 797,66 797,67 0,65"/>
    <polygon class="slate" points="0,37 560,58 0,59"/>
    <polygon class="navy" points="0,0 797,0 797,66 0,37"/>
  </svg>
  <div class="brand">
    <div class="brand-ring"></div>
    <div class="brand-name">Larchmont Realty</div>
  </div>
  <div class="return-address">48 Linden Court • Maple Ridge • State • 54321</div>
</section>

</body>
</html>
```